Business Card Design (NEW FILES)

ATTENTION: New vector files are available. Please update your design to reflect/use the new (better resolution) logo images.

Seeking a unique and professional business card design for a commercial drone photography/videography business. The layout should feature
the logo (attached) and include the following information:
978-512-6037
www.skyvantmedia.com
ORD Certified Remote Pilot

```html
<!DOCTYPE html>
<html lang="en">
<head>
<meta charset="utf-8">
<title>Skyvant Media – Business Card</title>
<link rel="stylesheet" href="https://fonts.googleapis.com/css2?family=Poppins:wght@400;500&display=swap">
<style>
  :root {
    --navy: #131a47;
    --orange: #e98e58;
    --white: #ffffff;
    --stage: #ababab;
    --ink: #1b1f3a;
    --rule: #c9c9c9;
  }
  * { margin: 0; padding: 0; box-sizing: border-box; }
  html, body {
    width: 1093px; height: 1200px; overflow: hidden;
    background: var(--stage);
    font-family: "Poppins", sans-serif;
  }
  .card {
    position: absolute; left: 265px;
    width: 578px; height: 357px;
    border-radius: 30px; overflow: hidden;
  }
  .card--front { top: 226px; background: var(--white); }
  .card--back { top: 621px; background: var(--navy); }

  .brand {
    position: absolute; display: flex; align-items: center;
  }
  .brand__name { font-weight: 500; letter-spacing: 0.04em; white-space: nowrap; }
  .brand__dot { border-radius: 50%; background: var(--orange); flex: none; }

  .card--front .brand { left: 40px; top: 175px; gap: 8px; }
  .card--front .brand__name { font-size: 22px; color: var(--navy); }
  .card--front .brand__dot { width: 12px; height: 12px; }

  .card--back .brand { left: 0; right: 0; top: 156px; justify-content: center; gap: 14px; }
  .card--back .brand__name { font-size: 42px; color: var(--white); }
  .card--back .brand__dot { width: 22px; height: 22px; }

  .divider {
    position: absolute; left: 291px; top: 107px;
    width: 1px; height: 142px; background: var(--rule);
  }
  .person { position: absolute; left: 313px; top: 117px; }
  .person__name { font-size: 24px; font-weight: 500; color: var(--navy); line-height: 1.1; letter-spacing: 0.01em; }
  .person__role { font-size: 15px; color: var(--orange); line-height: 1.2; }

  .contact { position: absolute; left: 313px; top: 190px; list-style: none; }
  .contact__item {
    display: flex; align-items: center; gap: 9px;
    font-size: 17px; color: var(--ink); line-height: 21px;
  }
  .contact__icon { width: 15px; height: 15px; flex: none; }

  .wave { position: absolute; left: 0; top: 0; width: 578px; height: 357px; }
  .credentials {
    position: absolute; left: 0; right: 0; top: 318px;
    text-align: center; font-size: 17px; color: var(--white);
    padding-left: 50px;
  }
  .credentials__sep { color: var(--orange); }
</style>
</head>
<body>
  <section class="card card--front">
    <svg class="wave" viewBox="0 0 578 357" aria-hidden="true">
      <path d="M6 349 Q289 232 572 341 L578 357 L0 357 Z" fill="var(--orange)"/>
      <path d="M8 352 Q289 242 572 344 L578 357 L0 357 Z" fill="var(--white)"/>
      <path d="M10 357 Q289 252 572 347 L578 357 Z" fill="var(--navy)"/>
    </svg>

    <div class="brand">
      <span class="brand__name">SKYVANT MEDIA</span>
      <span class="brand__dot"></span>
    </div>

    <div class="divider"></div>

    <div class="person">
      <p class="person__name">MARK DOYLE</p>
      <p class="person__role">OWNER</p>
    </div>

    <ul class="contact">
      <li class="contact__item">
        <svg class="contact__icon" viewBox="0 0 24 24" aria-hidden="true">
          <path d="M6.6 10.8a15.2 15.2 0 0 0 6.6 6.6l2.2-2.2a1 1 0 0 1 1-.25 11.4 11.4 0 0 0 3.6.57 1 1 0 0 1 1 1V20a1 1 0 0 1-1 1A17 17 0 0 1 3 4a1 1 0 0 1 1-1h3.5a1 1 0 0 1 1 1c0 1.25.2 2.45.57 3.57a1 1 0 0 1-.25 1z" fill="none" stroke="var(--ink)" stroke-width="2"/>
          <path d="M14 3a7 7 0 0 1 7 7M14 7a3 3 0 0 1 3 3" fill="none" stroke="var(--ink)" stroke-width="2" stroke-linecap="round"/>
        </svg>
        <span>978-512-6037</span>
      </li>
      <li class="contact__item">
        <svg class="contact__icon" viewBox="0 0 24 24" aria-hidden="true">
          <g fill="none" stroke="var(--ink)" stroke-width="2">
            <circle cx="12" cy="12" r="10"/>
            <ellipse cx="12" cy="12" rx="4.5" ry="10"/>
            <path d="M2 12h20M4 6.5h16M4 17.5h16"/>
          </g>
        </svg>
        <span>www.skyvantmedia.com</span>
      </li>
    </ul>

    <p class="credentials">ORD Certified Remote Pilot <span class="credentials__sep">|</span> Fully Insured</p>
  </section>

  <section class="card card--back">
    <div class="brand">
      <span class="brand__name">SKYVANT MEDIA</span>
      <span class="brand__dot"></span>
    </div>
  </section>
</body>
</html>
```